Wordpress Theme Design for Glacio-Blaze

Hi, I am looking for an awesome WORDPRESS theme for my snoball and coffee business that is called Glacio-Blaze. This has to be a wordpress theme, because I have other plugins that I would like to use with this site. I want the design to be professional and sophisticated, but also appeal to kids, because after all, the main focus of the business is going to be snoballs, which kids love. I don't want it to look too much like a kiddy site, though. I am also going to be selling other items such as frito pies, hotdogs, cotton candy, nachos, pickles, candy, toys, etc, but the main focus will be the hot and cold aspect of the coffee and snoballs (hence the name, "Glacio-Blaze"). I want the design to look very creative/original and really be attractive to kids, but also very professional so that even adults like coming to the site.
Somewhere in the design I would like to be able to advertise other local businesses in the future, so I would like space incorporated into the design for that. I would also like to be able to add other pages if I want, so there should be space along the top for links, such as "home", "contact", etc. It would also be nice to have a footer in the design for links or other plugins. If you take a look at the site http://quirkypuppyclipsz.example/, I like the functionality of the site (for example, the layout, links, footer, sidebar on other pages), but obviously there isn't much custom design with the theme.
I actually already have a logo designed that I would like incorporated into the look and feel of the design, so that should give you a good place to start with your design. I want the graphics in the theme to really be eye-catching. You are more than welcome to tweak my current logo, blend it into the theme, whatever...(if you want half of the page to be frozen, and the other half to be fire-ish, doesn't have to be, just giving ideas...any and all designs I will take into consideration). Basically, whatever you think would look amazing.
The more amazing the design, I would definitely give a bonus for.
If this helps you out, I'm not looking for a "glossy" style of wordpress design. I really like how this site (CraftHerdly) is made. It uses softer, cleaner colors and designs...it's kind of like a "grunge" style with its text and designs (what I mean is it's not a cookie cutter type of design), but nothing too extreme grunge by any means. I'm looking for the same style as the CraftHerdly site, only with the flare of my type of business.
Hope this helps
Thank you
Reason: The designs, although nice, are not really what I am looking for. These all just feel like they are ready made templates, and I'm looking for something a little more original and unique.

```html
<!DOCTYPE html>
<html lang="en">
<head>
<meta charset="utf-8">
<title>Glacio-Blaze – Snoballs and Coffee</title>
<link rel="stylesheet" href="https://fonts.googleapis.com/css2?family=PT+Sans:ital,wght@0,400;0,700;1,400&family=Ubuntu:wght@400;500&display=swap">
<style>
:root{
  --page:#f3f3f2;
  --ink:#3a2622;
  --body-text:#5a4a46;
  --brown-dark:#331c18;
  --sky:#33c3f0;
  --nav-top:#46c9f0;
  --nav-bottom:#169fd6;
  --link-blue:#1b98d5;
  --red:#e01a1a;
  --panel:#ececec;
  --card:#ffffff;
  --rule:#b8a8a5;
  --footer-text:#d9cfcc;
}
*{box-sizing:border-box;margin:0;padding:0}
html,body{width:960px;height:1200px;overflow:hidden}
body{background:var(--page);font-family:"PT Sans",Arial,sans-serif;color:var(--body-text);position:relative;border-top:3px solid var(--brown-dark)}
a{text-decoration:none;color:inherit}
.wrap{position:absolute;left:104px;width:751px}

/* header */
.brand{position:absolute;left:107px;top:70px;display:flex;align-items:center;gap:10px}
.brand-mark{width:30px;height:30px;border-radius:50%;background:var(--sky)}
.brand-name{font-family:"PT Sans",sans-serif;font-weight:700;font-size:30px;color:var(--ink)}
.brand-tag{position:absolute;left:147px;top:106px;font-size:9px;letter-spacing:2px;color:var(--ink)}
.util-links{position:absolute;right:105px;top:14px;font-size:11px;color:var(--ink)}
.util-links span{margin:0 5px;color:#777}
.search{position:absolute;left:488px;top:87px;width:175px;height:23px;display:flex}
.search-field{flex:1;background:#ececec;border:1px solid #c9c9c9;border-right:0;border-radius:2px 0 0 2px}
.search-btn{width:28px;background:var(--red);border-radius:0 2px 2px 0;display:flex;align-items:center;justify-content:center}
.call{position:absolute;left:716px;top:68px;color:var(--ink)}
.call-label{font-size:15px}
.call-number{font-size:24px;line-height:28px}

/* navigation */
.nav{top:142px;height:36px;display:flex;background:linear-gradient(var(--nav-top),var(--nav-bottom));border-radius:3px 3px 0 0;border:1px solid #1395cc}
.nav a{display:flex;align-items:center;justify-content:center;color:#fff;font-weight:700;font-size:12.5px;border-right:1px solid #1a8fc2;box-shadow:inset 1px 0 0 rgba(255,255,255,.25)}
.nav a:last-child{border-right:0}

/* hero */
.hero-band{position:absolute;left:0;top:178px;width:960px;height:335px;background:var(--sky);border-bottom:1px solid #1e9fcf}
.hero{top:178px;height:358px;background:linear-gradient(100deg,#6b5a55 0%,#b8928a 30%,#c85a4f 55%,#d7cfc8 80%,#9d8f88 100%);box-shadow:0 12px 14px -8px rgba(0,0,0,.45)}
.hero-dots{position:absolute;left:345px;bottom:8px;display:flex;gap:4px}
.hero-dots i{width:18px;height:18px;border-radius:50%;background:radial-gradient(circle at 40% 35%,#fff,#a9a9a9);display:block}
.hero-dots i.active{background:radial-gradient(circle at 40% 35%,#ff5d5d,#c40f0f)}
.divider{top:576px;height:3px;background:var(--rule)}

/* content */
.welcome{position:absolute;left:104px;top:596px;width:495px;height:166px;background:var(--panel);border-radius:4px;padding:10px 15px}
h2{font-family:"Ubuntu",sans-serif;font-weight:400;color:var(--ink);font-size:20px}
.welcome-photo{position:absolute;left:15px;top:42px;width:112px;height:96px;border-radius:3px;background:linear-gradient(135deg,#7a5440,#c7a37b 50%,#6c7d85)}
.welcome-text{position:absolute;left:140px;top:42px;width:340px;font-size:11px;line-height:18.5px}
.lead{color:var(--link-blue);font-weight:700}
.btn-red{display:inline-block;margin-top:6px;background:var(--red);color:#fff;font-size:11px;font-weight:700;padding:1px 10px 2px;border-radius:3px}

.card{position:absolute;top:779px;width:241px;height:224px;background:var(--card);border:1px solid #dedede;border-radius:4px;box-shadow:0 1px 3px rgba(0,0,0,.12);padding:12px 6px 12px 14px}
.card.testimonials{left:104px}
.card.serve{left:359px}
.item{position:relative;display:flex;gap:11px;margin-top:10px}
.thumb{width:61px;height:55px;border-radius:3px;flex:none}
.item h3{font-size:12px;font-weight:700;color:var(--link-blue)}
.item p{font-size:10.5px;line-height:14.5px;width:132px}
.testimonials .item+.item{border-top:1px solid #ddd;padding-top:13px;margin-right:8px}
.serve .thumb{width:74px;height:66px}
.serve .item p{width:136px}
.serve .item h3{font-family:"Ubuntu",sans-serif;font-weight:400;font-size:13px;color:var(--red)}
.serve .item+.item{margin-top:24px}
.read-all{position:absolute;left:14px;bottom:12px;color:var(--red);font-weight:700;font-size:12px}

.products{position:absolute;left:628px;top:590px;width:227px}
.products h2{font-size:21px}
.product{display:flex;gap:15px;height:103px;padding-top:11px;border-bottom:1px solid #dcdcdc}
.product:last-child{border-bottom:0}
.product .thumb{width:77px;height:69px;border:2px solid #fff;box-shadow:0 0 0 1px #d4d4d4}
.product h3{font-size:12px;font-weight:700;color:var(--link-blue)}
.product p{font-size:10.5px;line-height:14px}
.price{display:inline-block;margin-top:6px;color:var(--red);font-weight:700;font-size:14px;border-bottom:1px solid var(--red);line-height:15px}

/* footer */
.footer{position:absolute;left:0;top:1027px;width:960px;height:173px;background:var(--brown-dark);color:var(--footer-text)}
.footer h4{font-weight:700;font-size:15px;color:#fff}
.f-news{position:absolute;left:104px;top:14px;width:215px}
.f-news p{font-size:10.5px;line-height:16px;margin-top:8px}
.f-meta{display:flex;justify-content:space-between;margin-top:14px;font-size:9.5px;color:#2fb6ea}
.f-readall{display:block;margin-top:16px;color:var(--red);font-weight:700;font-size:11px}
.f-links{position:absolute;left:364px;top:17px;font-size:9.5px;line-height:18.5px;color:#eee}
.f-social{position:absolute;left:491px;top:13px;font-size:9.5px;color:#eee}
.f-social li{list-style:none;display:flex;align-items:center;gap:8px;height:29px}
.f-social i{width:19px;height:19px;border-radius:50%;display:block}
.f-mini-brand{position:absolute;left:604px;top:120px;font-size:12px;font-weight:700;color:#8a7d7a}
.f-news-letter{position:absolute;left:679px;top:14px;width:176px}
.f-email{margin-top:11px;height:25px;background:#5a4541;border-radius:3px;font-style:italic;font-size:11px;color:#b4a8a5;padding:5px 11px}
.f-send{position:absolute;right:0;top:78px;background:var(--link-blue);color:#fff;font-weight:700;font-size:12px;padding:3px 12px;border-radius:2px}
.f-copy{position:absolute;left:3px;top:122px;font-size:9.5px;line-height:16px;width:180px}
</style>
</head>
<body>
<header>
  <div class="brand"><span class="brand-mark"></span><span class="brand-name">Glacio-Blaze</span></div>
  <div class="brand-tag">SNOBALLS and COFFEE</div>
  <div class="util-links"><a href="#">Login</a><span>|</span><a href="#">Register</a><span>|</span><a href="#">Site Map</a></div>
  <form class="search">
    <div class="search-field"></div>
    <div class="search-btn"><svg width="14" height="14" viewBox="0 0 14 14"><circle cx="5.5" cy="5.5" r="4" fill="none" stroke="#fff" stroke-width="2"/><line x1="8.5" y1="8.5" x2="13" y2="13" stroke="#fff" stroke-width="2.5"/></svg></div>
  </form>
  <div class="call"><div class="call-label">Call Us:</div><div class="call-number">123 456 7890</div></div>
</header>

<nav class="wrap nav">
  <a href="#" style="width:84px">Home</a>
  <a href="#" style="width:95px">About Us</a>
  <a href="#" style="width:96px">Services</a>
  <a href="#" style="width:75px">Shop</a>
  <a href="#" style="width:111px">Testimonials</a>
  <a href="#" style="width:120px">News &amp; Events</a>
  <a href="#" style="width:69px">Blog</a>
  <a href="#" style="flex:1">Contact Us</a>
</nav>

<div class="hero-band"></div>
<section class="wrap hero" role="img" aria-label="Photo of a layered macchiato and a small cup of coffee on saucers in a café with red chairs">
  <div class="hero-dots"><i class="active"></i><i></i><i></i></div>
</section>
<div class="wrap divider"></div>

<section class="welcome">
  <h2>Welcome to GlacioBlaze</h2>
  <div class="welcome-photo" role="img" aria-label="Photo of the shop counter with a display case"></div>
  <div class="welcome-text">
    <p class="lead">Aliquam molestie, mi et imperdiet euismod, dui purus auctor tellus.</p>
    <p>Sed accumsan sollicitudin sapien, sit amet adipiscing turpis gravida ac. In congue, neque ac lobortis volutpat, libero mauris varius mi, vitae suscipit ipsum ligula vitae risus. Duis aliquam nibh a dui iaculis viverra id a velit. Vivamus egestas risus in magna varius commodo.</p>
    <a class="btn-red" href="#">Read More</a>
  </div>
</section>

<section class="card testimonials">
  <h2>Testimonials</h2>
  <div class="item">
    <div class="thumb" role="img" aria-label="Photo of a cup of coffee with pastries" style="background:linear-gradient(135deg,#8a4a2a,#e8d2b5)"></div>
    <div><h3>Theo Marlow</h3><p>Vestibulum ante ipsum primis in faucibus orci luctus et ultrices posuere........</p></div>
  </div>
  <div class="item">
    <div class="thumb" role="img" aria-label="Photo of a hand holding a rainbow snoball cup" style="background:linear-gradient(135deg,#6f9fd8,#e86a4a 55%,#f0e8e0)"></div>
    <div><h3>Lena Brook</h3><p>Vestibulum ante ipsum primis in faucibus orci luctus et ultrices posuere........</p></div>
  </div>
  <a class="read-all" href="#">Read All</a>
</section>

<section class="card serve">
  <h2>What we Serve</h2>
  <div class="item">
    <div class="thumb" role="img" aria-label="Photo of a cappuccino surrounded by coffee beans" style="background:linear-gradient(135deg,#3b2215,#d9c3a4 60%,#5a3220)"></div>
    <div><h3>About Coffee</h3><p>Aliquam ullamcorper tempor felis, nec condimentum odio aliquet vitae.</p></div>
  </div>
  <div class="item">
    <div class="thumb" role="img" aria-label="Photo of a yellow snoball in a cup" style="background:linear-gradient(135deg,#2a2a2a,#f2d24a 55%,#1d1d1d)"></div>
    <div><h3>About Snowball</h3><p>Aliquam ullamcorper tempor felis, nec condimentum odio aliquet vitae.</p></div>
  </div>
</section>

<aside class="products">
  <h2>Products</h2>
  <div class="product">
    <div class="thumb" role="img" aria-label="Photo of a latte with foam art" style="background:linear-gradient(135deg,#3a2418,#c89a6a 55%,#efe6dc)"></div>
    <div><h3>Product 1</h3><p>Lorem ipsum dolor sit amet, consectetur adipiscing elit.</p><span class="price">$5.00</span></div>
  </div>
  <div class="product">
    <div class="thumb" role="img" aria-label="Photo of a cappuccino on a red table" style="background:linear-gradient(135deg,#7a1010,#d99a5a 55%,#f4ece4)"></div>
    <div><h3>Product 2</h3><p>Lorem ipsum dolor sit amet, consectetur adipiscing elit.</p><span class="price">$2.00</span></div>
  </div>
  <div class="product">
    <div class="thumb" role="img" aria-label="Photo of green, yellow and red snoballs in cups" style="background:linear-gradient(135deg,#7ed04a,#f0e040 50%,#c24a3a)"></div>
    <div><h3>Product 3</h3><p>Lorem ipsum dolor sit amet, consectetur adipiscing elit.</p><span class="price">$8.00</span></div>
  </div>
  <div class="product">
    <div class="thumb" role="img" aria-label="Photo of chocolate truffles on a glass plate" style="background:linear-gradient(135deg,#5ec4c8,#5a3a30 55%,#a8dede)"></div>
    <div><h3>Product 4</h3><p>Lorem ipsum dolor sit amet, consectetur adipiscing elit.</p><span class="price">$5.00</span></div>
  </div>
</aside>

<footer class="footer">
  <div class="f-news">
    <h4>News &amp; Events</h4>
    <p>Nam fermentum vestibulum purus id aliquet. Phasellus dui ante, ultricies et sollicitudin pretium, fermentum vel velit...</p>
    <div class="f-meta"><a href="#">Read More</a><span>Posted on Aug18, 2012</span></div>
    <a class="f-readall" href="#">Read All</a>
  </div>
  <nav class="f-links">
    <a href="#">Home</a><br><a href="#">About Us</a><br><a href="#">Services</a><br><a href="#">Shop</a><br><a href="#">Testimonials</a><br><a href="#">News &amp; Events</a><br><a href="#">Blog</a><br><a href="#">Contact Us</a>
  </nav>
  <ul class="f-social">
    <li><i style="background:#2e4f8a"></i>Friendbook</li>
    <li><i style="background:#2cb3e6"></i>Chirper</li>
    <li><i style="background:#555"></i>Circleplus</li>
    <li><i style="background:#c8232c"></i>Pinboardly</li>
    <li><i style="background:#f0902a"></i>Rss Feed</li>
  </ul>
  <div class="f-mini-brand">Glacio-Blaze</div>
  <div class="f-news-letter">
    <h4>Newsletter SignUp</h4>
    <div class="f-email">enter email address</div>
    <a class="f-send" href="#">Send</a>
    <div class="f-copy">Copyright ©2012 GlacioBlaze.example<br>All Right Reserved &nbsp;|&nbsp; Privacy Policy</div>
  </div>
</footer>
</body>
</html>
```